依頼詳細
メール便発送用の商品配送封筒のデザインをお願い致します。
サイズ:角A4封筒
用紙種類:クラフト紙
印刷範囲:外側両面(袋の中へのデザインは不要です)

※クラフト紙への印刷になるため、白系統の色がそのまま発色しません。そのあたりを考慮したなるべくクラフト紙にデザイン経験のあるかたを選考有利に進めさせていただきます。
記載項目
表面
【メッセージ】
お客様へ
いつも青葉ライフケアをご利用いただきましてありがとうございます。
弊社の商品やサービスを通してお客様の人生のサポートになれば幸いです。

もしご不明点やご質問がございましたら、いつでもお気軽にお問い合わせください。お客様のお悩みに合わせたお返事ができるよう尽力してまいります。

商品をご配送いただく方へ
弊社商品は衝撃で崩れてしまうような商品もありますので何卒優しめにお取り扱いください。
配送したいただく方のお陰様でお客様のお役に立つことができております。
いつも弊社商品を運んでいただきありがとうございます。

【ブランドロゴ】

【配送住所】
〒812-3056 福岡県糸島市瀬川205-3 青葉ライフケア配送センター

【電話番号】TEL:0120-374-621(平日9:00~17:00)土日祝休み

【URL】

【QRコード】
上記URLのQRコード

裏面
【メッセージ】
「みんなにとってのSDGS」
今回のお届けよりお届けのしやすさ、捨てやすさ、より環境に配慮した封筒タイプに変更いたしました。
希望イメージ
シンプル 複雑
単色 カラフル
暗い 明るい
日常 高級
遊び心 厳粛
未来的 伝統的
女性的 男性的
希望する色
納品ファイル
• 高解像度JPG (.jpg)
• イラストレーター形式 (.ai)
• フォトショップ形式 (.psd)
補足説明
URL欄はあけておいてデザインお願い致します。
他社様の封筒デザイン例をファイルにアップしています。

ロゴを枠にするアイデアがいいと思いました。

この度は弊社コンペにご参加いただきありがとうございました。
今後も定期的にコンペを行いますのでタイミングが合えばぜひご参加ください。

```html
<!DOCTYPE html>
<html lang="ja">
<head>
<meta charset="utf-8">
<title>青葉ライフケア 配送封筒</title>
<link rel="stylesheet" href="https://fonts.googleapis.com/css2?family=Zen+Maru+Gothic:wght@500;700&family=Noto+Sans+JP:wght@400;700&display=swap">
<style>
  :root {
    --kraft: #c9b290;
    --kraft-deep: #b59b74;
    --flap: #2c4a2e;
    --flap-text: #e6d8b6;
    --ink: #3a5236;
    --ink-soft: #4f6348;
    --leaf: #6f8a5e;
    --leaf-deep: #4f6b45;
    --blossom: #c98c8c;
    --gold: #b8975a;
    --accent: #d9822b;
    --stage: #ffffff;
  }
  * { margin: 0; padding: 0; box-sizing: border-box; }
  html, body { width: 882px; height: 1200px; overflow: hidden; background: var(--stage); }
  .envelope {
    position: relative; width: 882px; height: 1200px;
    background: var(--kraft); overflow: hidden;
    font-family: "Zen Maru Gothic", "Noto Sans JP", sans-serif; color: var(--ink);
  }
  .flap {
    position: absolute; left: 0; top: 0; width: 882px; height: 100px;
    background: var(--flap); color: var(--flap-text);
    display: flex; flex-direction: column; align-items: center; justify-content: center; gap: 8px;
    transform: rotate(180deg);
  }
  .flap-note { font-size: 11px; letter-spacing: .05em; font-family: "Noto Sans JP", sans-serif; }
  .flap-title { font-size: 19px; font-weight: 700; letter-spacing: .08em; }
  .greenery { position: absolute; border-radius: 50%; filter: blur(6px); }
  .greenery-left {
    left: -60px; top: 230px; width: 330px; height: 900px;
    background: radial-gradient(ellipse at 40% 50%, rgba(79,107,69,.75), rgba(111,138,94,.45) 55%, rgba(111,138,94,0) 75%);
  }
  .greenery-top {
    left: 210px; top: 110px; width: 560px; height: 260px;
    background: radial-gradient(ellipse at 60% 40%, rgba(111,138,94,.6), rgba(201,140,140,.2) 55%, rgba(111,138,94,0) 75%);
  }
  .greenery-right {
    right: -70px; top: 420px; width: 300px; height: 380px;
    background: radial-gradient(ellipse at 50% 50%, rgba(111,138,94,.55), rgba(111,138,94,0) 72%);
  }
  .greenery-bottom {
    right: 40px; bottom: 40px; width: 440px; height: 320px;
    background: radial-gradient(ellipse at 55% 55%, rgba(79,107,69,.7), rgba(111,138,94,.35) 55%, rgba(111,138,94,0) 75%);
  }
  .bow {
    position: absolute; left: 140px; top: 300px; width: 140px; height: 120px; border-radius: 50%;
    background: radial-gradient(circle, #c9ab6a, #a88a4c 60%, rgba(168,138,76,0) 72%);
  }
  .frame { position: absolute; left: 0; top: 0; }
  .message { position: absolute; left: 270px; width: 350px; text-align: center; }
  .message h2 { font-size: 15px; font-weight: 700; margin-bottom: 8px; letter-spacing: .05em; }
  .message p { font-size: 11px; line-height: 1.75; color: var(--ink-soft); font-family: "Noto Sans JP", sans-serif; }
  .message-customer { top: 505px; }
  .message-carrier { top: 848px; }
  .brand { position: absolute; left: 300px; top: 690px; display: flex; align-items: center; gap: 10px; }
  .brand-dot { width: 34px; height: 34px; border-radius: 50%; background: var(--accent); }
  .brand-name { font-size: 22px; font-weight: 700; color: var(--ink); letter-spacing: .04em; }
  .phone { position: absolute; left: 300px; top: 745px; display: flex; align-items: center; gap: 8px; }
  .phone-number { font-size: 30px; font-weight: 700; color: var(--accent); letter-spacing: .02em; }
  .contact-notes {
    position: absolute; left: 270px; top: 792px; width: 350px; text-align: center;
    font-size: 9px; line-height: 1.6; color: var(--ink-soft); font-family: "Noto Sans JP", sans-serif;
  }
  .care-marks { position: absolute; left: 560px; top: 668px; display: grid; grid-template-columns: 24px 24px; gap: 6px; }
  .care-mark { width: 24px; height: 24px; background: var(--ink-soft); border-radius: 3px; display: flex; align-items: center; justify-content: center; }
</style>
</head>
<body>
<main class="envelope">
  <header class="flap">
    <p class="flap-note">今回のお届けより、お届けのしやすさ・捨てやすさ、より環境に配慮した封筒タイプに変更いたしました。</p>
    <p class="flap-title">「みんなにとってのSDGS」</p>
  </header>

  <div class="greenery greenery-left" role="img" aria-label="左側を縁取る水彩の葉と小花のボタニカル装飾"></div>
  <div class="greenery greenery-top" role="img" aria-label="上部の葉と小花のボタニカル装飾"></div>
  <div class="greenery greenery-right" role="img" aria-label="右側の葉のボタニカル装飾"></div>
  <div class="greenery greenery-bottom" role="img" aria-label="右下の葉と枝のボタニカル装飾"></div>
  <div class="bow" role="img" aria-label="金色のギフトリボン"></div>

  <svg class="frame" width="882" height="1200" viewBox="0 0 882 1200" aria-hidden="true">
    <polyline points="250,470 441,300 640,470 640,1010 441,1120 250,1010 250,470" fill="none" stroke="var(--gold)" stroke-width="1.4"/>
    <polyline points="270,480 441,330 620,480 620,1000 441,1095 270,1000 270,480" fill="none" stroke="var(--gold)" stroke-width=".8" opacity=".7"/>
  </svg>

  <section class="message message-customer">
    <h2>お客様へ</h2>
    <p>いつも青葉ライフケアをご利用いただきまして<br>ありがとうございます。<br>弊社の商品やサービスを通して<br>お客様の人生のサポートになれば幸いです。<br>もしご不明点やご質問がございましたら、<br>いつでもお気軽にお問い合わせください。</p>
  </section>

  <div class="brand">
    <span class="brand-dot"></span>
    <span class="brand-name">青葉ライフケア</span>
  </div>

  <div class="care-marks">
    <span class="care-mark"><svg width="16" height="16" viewBox="0 0 16 16"><path d="M8 2v12M4 6l4-4 4 4" stroke="var(--kraft)" stroke-width="1.6" fill="none"/></svg></span>
    <span class="care-mark"><svg width="16" height="16" viewBox="0 0 16 16"><path d="M2 8a6 6 0 0 1 12 0ZM8 8v5" stroke="var(--kraft)" stroke-width="1.4" fill="none"/></svg></span>
    <span class="care-mark"><svg width="16" height="16" viewBox="0 0 16 16"><path d="M5 2h6l-1 6H6ZM8 8v5M5 14h6" stroke="var(--kraft)" stroke-width="1.4" fill="none"/></svg></span>
    <span class="care-mark"><svg width="16" height="16" viewBox="0 0 16 16"><rect x="3" y="4" width="10" height="9" stroke="var(--kraft)" stroke-width="1.4" fill="none"/></svg></span>
  </div>

  <div class="phone">
    <svg width="26" height="26" viewBox="0 0 24 24" aria-hidden="true"><path d="M6.6 10.8a15 15 0 0 0 6.6 6.6l2.2-2.2a1 1 0 0 1 1-.25 11.4 11.4 0 0 0 3.6.6 1 1 0 0 1 1 1V20a1 1 0 0 1-1 1A17 17 0 0 1 3 4a1 1 0 0 1 1-1h3.5a1 1 0 0 1 1 1c0 1.25.2 2.45.6 3.6a1 1 0 0 1-.25 1Z" fill="var(--accent)"/></svg>
    <span class="phone-number">0120-374-621</span>
  </div>

  <p class="contact-notes">TEL 平日9:00〜17:00（土日祝休み）<br>〒812-3056 福岡県糸島市瀬川205-3 青葉ライフケア配送センター</p>

  <section class="message message-carrier">
    <h2>商品をご配送いただく方へ</h2>
    <p>弊社商品は衝撃で崩れてしまうような商品もありますので<br>何卒優しめにお取り扱いください。<br>配送していただく方のお陰様で<br>お客様のお役に立つことができております。<br>いつも弊社商品を運んでいただきありがとうございます。</p>
  </section>
</main>
</body>
</html>
```